Unique Flyer Project - www.plumvaleforms.com.au

The purpose of this flyer is trying to get recipients to visit the website www.plumvaleforms.com.au and sign up to the offer. I need it to be simple/to the point, eye catching and professional. I will post up a basic idea I have but feel free to put your own spin on it if you think you have great ideas to get people to visit the site, if not then just improve upon the quality of mine and make it look like a respected company.

I also think a red band or something that REALLY catches the eye highlighting one of the important aspects of the flyer (the domain?) could be great so even if someone is about to put it in the bin, the popping red-on-white-background catches their eye so they end up looking at and reading the flyer.

I would also love a VERY SIMPLE design for the backside of the flyer, just a red box/band (whatever you think is good) with the domain 'www.plumvaleforms.com.au' in it. NOTHING ELSE! Just so if it's floating around the table and it's upside down, there's something eye catching that might entice the householder to look at it.

DESIGN IS FOR DL FLYER: 99mm X 210mm

Target Market(s)

Australian Residents interested in earning money from home.

Industry/Entity Type

It Company

Requirements
Must have
• Eye catching (mainly red band/box/bar on front & back page), SIMPLE, elegant/professional.
Should not have
• ANYTHING unnecessary to the reader that will distract them from the ultimate point - GET PAID TO DO SURVEYS FROM YOUR OWN HOME ON THE COMPUTER!

```html
<!DOCTYPE html>
<html lang="en">
<head>
<meta charset="utf-8">
<title>Plumvale Forms – DL Flyer Front</title>
<link rel="stylesheet" href="https://fonts.googleapis.com/css2?family=Roboto+Condensed:wght@400;700&display=swap">
<style>
  :root {
    --paper: #ffffff;
    --ink: #111111;
    --frame: #555555;
    --brand-blue: #1f5fae;
    --accent-red: #d11a14;
    --band-dark: #8e0d0c;
    --band-mid: #c2141a;
    --band-light: #d9383a;
    --photo-hair: rgba(58, 34, 24, 0.55);
    --photo-top: rgba(30, 26, 26, 0.75);
    --flag-blue: #13257a;
    --cash-green: rgba(120, 140, 105, 0.55);
    --cash-light: rgba(200, 208, 180, 0.35);
  }
  * { box-sizing: border-box; margin: 0; padding: 0; }
  html, body {
    width: 1200px; height: 566px; overflow: hidden;
    background: var(--paper);
  }
  .flyer {
    position: relative;
    width: 1200px; height: 566px;
    background: var(--paper);
    border: 2px solid var(--frame);
    overflow: hidden;
    font-family: "Roboto Condensed", "Arial Narrow", sans-serif;
    color: var(--ink);
  }
  .promo-band {
    position: absolute;
    left: 0; top: 452px;
    width: 1010px; height: 70px;
    background: linear-gradient(90deg, var(--band-dark) 0%, var(--band-mid) 45%, var(--band-light) 100%);
  }
  .promo-band__url {
    position: absolute;
    left: 0; right: 0; top: 0;
    line-height: 70px;
    padding-left: 190px;
    text-align: center;
    color: var(--paper);
    font-size: 38px;
    font-weight: 400;
  }
  .model-photo {
    position: absolute;
    left: 60px; top: 30px;
    width: 290px; height: 536px;
    background:
      radial-gradient(ellipse 42% 22% at 50% 22%, var(--photo-hair) 0%, rgba(58,34,24,0) 100%),
      radial-gradient(ellipse 50% 60% at 50% 75%, var(--photo-top) 0%, rgba(30,26,26,0.45) 65%, rgba(30,26,26,0) 100%);
  }
  .brand-name {
    position: absolute;
    left: 370px; top: 78px;
    width: 420px;
    text-align: center;
    font-size: 66px;
    font-weight: 700;
    line-height: 1;
    color: var(--brand-blue);
  }
  .country-badge {
    position: absolute;
    left: 1007px; top: 28px;
    width: 156px;
    text-align: center;
  }
  .country-badge__flag {
    width: 156px; height: 92px;
    background: linear-gradient(135deg, var(--flag-blue), #1d3596);
  }
  .country-badge__label {
    margin-top: 12px;
    font-size: 27px;
    line-height: 34px;
  }
  .pitch {
    position: absolute;
    left: 380px; width: 730px;
    text-align: center;
    font-weight: 400;
  }
  .pitch__headline {
    top: 234px;
    font-size: 46px;
    line-height: 56px;
  }
  .pitch__details {
    top: 310px;
    font-size: 34px;
    line-height: 52px;
  }
  .pitch__amount {
    color: var(--accent-red);
    font-weight: 700;
    font-size: 44px;
  }
  .cash-stack {
    position: absolute;
    left: 905px; top: 400px;
    width: 295px; height: 166px;
    background: radial-gradient(ellipse 60% 55% at 60% 60%, var(--cash-green) 0%, var(--cash-light) 60%, rgba(255,255,255,0) 100%);
  }
</style>
</head>
<body>
  <main class="flyer">
    <div class="promo-band">
      <p class="promo-band__url">www.plumvaleforms.com.au</p>
    </div>

    <div class="model-photo" role="img" aria-label="Photo of a surprised young woman with curly hair in a black top, hands on her cheeks"></div>

    <h1 class="brand-name">Plumvale Forms</h1>

    <div class="country-badge">
      <div class="country-badge__flag" role="img" aria-label="Australian flag"></div>
      <p class="country-badge__label">NOW OPEN<br>AUSTRALIA</p>
    </div>

    <h2 class="pitch pitch__headline">Could You Use An Extra Income?</h2>
    <p class="pitch pitch__details">
      Earn as much as <span class="pitch__amount">$50</span> per survey!<br>
      Work from home and choose your hours!
    </p>

    <div class="cash-stack" role="img" aria-label="Stacks of banded banknotes"></div>
  </main>
</body>
</html>
```